On-Hold Advertising & Music Business needs logo design

Our umbrella name is Larkfen Sound Collective. Our main focus is providing custom on hold advertising and music (plays to callers on hold and businesses all over North America and Canada) The name of the company under this umbrella name is (and has been for 30 years) Quillmere Tones. We pioneered the on hold marketing/advertising industry in the mid 80's. The final design should communicate CREATIVE ADVERTISING & MUSIC SPECIFIC TO THE ON HOLD APPLICATION. In addition to ON HOLD MUSIC AND MESSAGING, The company offers IN-BUILDING (OVERHEAD) MUSIC, DIGITAL SIGNAGE, AND access to PROFESSIONAL VOICE TALENT including MULTILINGUAL TALENT. The card can be (but doesn't have to be) double sided. I would like to see something on the front side that screams ADVERTISING FOR THE ON HOLD ENVIRONMENT, and then perhaps the balance of what we offer on the back side? We create an audio portrait of a busiiness through messages that play to the business' callers while on hold. I hjave included our current logo but I am open to new logo ideas if it doesn't fit well on a card.

Target Market(s)

Businesses of all kinds, shapes and sizes. Owners, Managers, Representatives from the companies

Industry/Entity Type

Advertising

Contact Information for Business Card

We want the front side to scream CREATIVE on hold advertising and music. it should feature our logo and have our contact information on it. It should also have room for names of staff (one per card of course along with their title)

Colors

Designer to choose colors to be used in the design.

Requirements
Must have
• Nameof the company and it should be clear what we are leading with: CREATIVE ON HOLD ADVERTISING AND MUSIC. It should at least list (okay on the back) our other services: In-Building (overhead) Music, Digital Signage and access to Professional Voice Talent for IVR/Telephone prompts (multi-language talent too)
Should not have
• The card should not be crammed with information (or at least not look like it is)

```html
<!DOCTYPE html>
<html lang="en">
<head>
<meta charset="utf-8">
<title>Larkfen Sound Collective – Business Card</title>
<link rel="stylesheet" href="https://fonts.googleapis.com/css2?family=Alegreya:wght@400;500&family=Open+Sans:wght@400;600&display=swap">
<style>
  :root {
    --backdrop: #3b3532;
    --card-white: #ededee;
    --brand-red: #e01f27;
    --ink-slate: #2f3d47;
    --ink-grey: #4a4f54;
    --on-red: #ffffff;
  }
  * { margin: 0; padding: 0; box-sizing: border-box; }
  html, body {
    width: 1200px; height: 844px; overflow: hidden;
    background: var(--backdrop);
  }
  .stage {
    position: relative; width: 1200px; height: 844px;
    display: flex; align-items: center; justify-content: center; gap: 50px;
  }
  .card {
    position: relative; width: 525px; height: 300px;
    box-shadow: 0 8px 24px rgba(0,0,0,.35);
  }

  /* Front */
  .card-front {
    background: var(--card-white);
    font-family: "Open Sans", Arial, sans-serif;
    color: var(--ink-grey);
  }
  .brand-lockup {
    position: absolute; top: 34px; right: 32px;
    display: flex; align-items: center; gap: 12px;
  }
  .brand-dot { width: 40px; height: 40px; border-radius: 50%; background: var(--brand-red); flex: none; }
  .brand-names {
    font-weight: 600; color: var(--brand-red);
    font-size: 15px; line-height: 1.3; letter-spacing: .08em; text-transform: uppercase;
  }
  .contact {
    position: absolute; left: 34px; bottom: 30px;
  }
  .person-name { font-size: 22px; font-weight: 600; line-height: 1; letter-spacing: .02em; }
  .person-name .first { color: var(--brand-red); }
  .person-name .last { color: var(--ink-slate); }
  .person-title { font-size: 13px; color: var(--ink-grey); margin-top: 3px; }
  .contact-lines { margin-top: 14px; font-size: 13px; line-height: 1.65; }
  .contact-lines .label { color: var(--brand-red); font-weight: 600; }
  .contact-lines .web { color: var(--brand-red); }
  .contact-lines .gap { display: inline-block; width: 14px; }
  .address { margin-top: 12px; font-size: 13px; }

  /* Back */
  .card-back {
    background: var(--brand-red);
    color: var(--on-red);
    font-family: "Alegreya", Georgia, serif;
    text-align: center;
  }
  .back-title { margin-top: 48px; font-size: 20px; font-weight: 500; letter-spacing: .06em; text-transform: uppercase; }
  .back-subtitle { margin-top: 6px; font-size: 19px; }
  .specialties {
    display: flex; justify-content: center; gap: 26px;
    margin-top: 34px; text-align: left;
  }
  .specialties ul { list-style: none; }
  .specialties li {
    font-size: 13.5px; letter-spacing: .05em; text-transform: uppercase; line-height: 1.55;
    display: flex; align-items: center; gap: 8px;
  }
  .specialties li::before {
    content: ""; width: 7px; height: 7px; border-radius: 50%; background: var(--on-red); flex: none;
  }
</style>
</head>
<body>
<main class="stage">
  <section class="card card-front">
    <div class="brand-lockup">
      <span class="brand-dot"></span>
      <div class="brand-names">Larkfen Sound Collective<br>Quillmere Tones</div>
    </div>
    <div class="contact">
      <p class="person-name"><span class="first">DANA</span> <span class="last">WHITLOW</span></p>
      <p class="person-title">Managing Director</p>
      <p class="contact-lines">
        <span class="label">P:</span> 555-014-2290<span class="gap"></span><span class="label">F:</span> 555-014-2290<br>
        <span class="label">E:</span> hello@larkfensound.com<span class="gap"></span><span class="web">www.larkfensound.com</span>
      </p>
      <p class="address">1234, Address Goes Here Country Name, 123456</p>
    </div>
  </section>

  <section class="card card-back">
    <h1 class="back-title">Larkfen Sound Collective</h1>
    <p class="back-subtitle">specialties</p>
    <div class="specialties">
      <ul>
        <li>On Hold Advertising</li>
        <li>Music On Hold</li>
        <li>In-Office Music</li>
        <li>In-Store Messaging</li>
        <li>IVR/Voice Prompts</li>
      </ul>
      <ul>
        <li>Digital Signage</li>
        <li>TV For Business</li>
        <li>Commercial Production</li>
        <li>Media Buying</li>
      </ul>
    </div>
  </section>
</main>
</body>
</html>
```